Brightfold Systems
Business Card
Professional
Daniel Harcourt
Serious Games Specialist
52 Millbrook Lane Arnprior, Ontario K7S 2B9 Canada
d.harcourt@brightfoldsys.net
http://www.brightfoldsys.net
Our company designs, operates, and supports "Serious Games" for training military, law enforcement, and government. We would like our business card to reflect this audience while maintaining the "cool" and "edgy" side of video games.
Feel the Brightfold.

```html
<!DOCTYPE html>
<html lang="en">
<head>
<meta charset="utf-8">
<title>Brightfold Systems Business Card</title>
<link rel="stylesheet" href="https://fonts.googleapis.com/css2?family=Open+Sans:wght@400;600;700;800&display=swap">
<style>
  :root {
    --backdrop: #a9a9a9;
    --card-white: #ffffff;
    --card-black: #050505;
    --brand-blue: #1f7cc4;
    --ink: #2b2b2b;
    --ink-soft: #555555;
    --tag-white: #e8e8e8;
  }
  * { margin: 0; padding: 0; box-sizing: border-box; }
  html, body {
    width: 1200px; height: 751px; overflow: hidden;
    background: var(--backdrop);
    font-family: "Open Sans", Arial, sans-serif;
  }
  .stage { position: relative; width: 1200px; height: 751px; }

  .card { position: absolute; box-shadow: 0 3px 10px rgba(0,0,0,0.35); }

  /* Front */
  .card-front { left: 127px; top: 70px; width: 463px; height: 300px; background: var(--card-white); }
  .front-rule {
    position: absolute; left: 0; right: 0; top: 157px; height: 3px;
    background: var(--brand-blue);
  }
  .front-brand {
    position: absolute; left: 16px; top: 144px;
    display: flex; align-items: center; gap: 7px;
    background: var(--card-white); padding: 0 8px 0 6px; height: 30px;
  }
  .brand-dot { width: 20px; height: 20px; border-radius: 50%; background: var(--brand-blue); flex: none; }
  .brand-name {
    font-weight: 800; font-size: 21px; letter-spacing: 0.5px; line-height: 1;
    color: var(--brand-blue); text-transform: uppercase;
  }
  .contact { position: absolute; right: 34px; text-align: right; white-space: nowrap; }
  .contact-name { top: 100px; font-size: 19px; font-weight: 600; color: var(--brand-blue); line-height: 24px; }
  .contact-title { top: 134px; font-size: 11px; font-weight: 700; color: var(--ink); line-height: 16px; }
  .contact-address { top: 166px; font-size: 11px; line-height: 20px; color: var(--ink-soft); }
  .contact-line {
    right: 20px; font-size: 11px; line-height: 16px; color: var(--ink-soft);
    display: flex; align-items: center; gap: 5px;
  }
  .contact-line svg { width: 10px; height: 10px; flex: none; }
  .line-phone { top: 232px; }
  .line-email { top: 256px; }
  .line-web { top: 278px; }

  /* Back */
  .card-back { left: 602px; top: 398px; width: 461px; height: 322px; background: var(--card-black); }
  .back-brand {
    position: absolute; left: 118px; top: 74px;
    display: flex; align-items: center; gap: 12px;
  }
  .back-brand .brand-dot { width: 34px; height: 34px; }
  .back-brand .brand-name { font-size: 38px; }
  .tagline {
    position: absolute; left: 142px; top: 158px;
    font-size: 13px; font-weight: 600; letter-spacing: 0.5px; color: var(--tag-white);
  }
</style>
</head>
<body>
<div class="stage">
  <section class="card card-front">
    <div class="front-rule"></div>
    <div class="front-brand">
      <span class="brand-dot"></span>
      <span class="brand-name">Brightfold</span>
    </div>
    <p class="contact contact-name">Daniel Harcourt</p>
    <p class="contact contact-title">Serious Games Specialist</p>
    <p class="contact contact-address">52 Millbrook Lane<br>Carrow Bay, Northvale<br>L2M 2B9 Canada</p>
    <p class="contact contact-line line-phone">613-555-0187
      <svg viewBox="0 0 10 10"><path d="M2 1 L4 1 L4.6 3 L3.4 4 Q4.4 6 6 6.6 L7 5.4 L9 6 L9 8 Q5 9 2 5 Q1 3 2 1Z" fill="var(--brand-blue)"/></svg>
    </p>
    <p class="contact contact-line line-email">d.harcourt@brightfoldsys.net
      <svg viewBox="0 0 10 10"><circle cx="5" cy="5" r="5" fill="var(--brand-blue)"/></svg>
    </p>
    <p class="contact contact-line line-web">http://www.brightfoldsys.net
      <svg viewBox="0 0 10 10"><circle cx="5" cy="5" r="5" fill="var(--brand-blue)"/></svg>
    </p>
  </section>

  <section class="card card-back">
    <div class="back-brand">
      <span class="brand-dot"></span>
      <span class="brand-name">Brightfold</span>
    </div>
    <p class="tagline">Feel the Brightfold.</p>
  </section>
</div>
</body>
</html>
```